依頼詳細
■依頼目的
本ブログの目的は、ミラボルト テクノサービスの認知拡大とブランディングとなります。
MTSの技術や最新動向への見解・取組を掲載する「MTS Tech ブログ」を立ち上げ、
中途採用 転職意向者 / ソリューション導入 検討者の意向を上げることを狙っております。

■デザインイメージ
ソラノート社運営ブログ「Buildnote.JX」
http://dev.soranote-example.jp/
制作注意点としまして、実装にはWordPressを使いますのでWordPressで実装が明らかにできないような
デザインは避けてください

■訴求ポイントの優先順位
1.ブログスペース
2.求人広告バナーエリア(自社のキャリア採用)

■ターゲット層
個人:中途採用 転職意向者
法人:ソリューション導入 検討者

■希望する色味
ミラボルトテクノサービスのトーン&マナーに合わせたもの
http://www.mts.mirabolt-example.co.jp/

■提供素材
ミラボルトテクノサービス:ロゴデーター

■納品ファイル
TOPページデザイン1点(PSDデータ)
ロゴの使用につきましては、添付のレギュレーションに従って作成をお願い致します。
デザインコンセプトにつきまして補足をさせて頂きます。TOPページのイメージとしまして一般的なブログ形式ではなく、デザインとレイアウトに関しましては最近のビジネスブログやキュレーションメディアのトレンドも考慮した先進性のあるデザインを考慮し、なおかつ読みやすい体裁での設計をお願いいたします。皆様からのご提案を心よりお待ちしております。よろしくお願いいたします。
ランサー様各位
この度は、たくさんの素晴らしいご提案を頂きましてありがとうございます。
さらにより多くの方からの魅力的なご応募を頂けるのではと思いまして
一週間延長の3/11(水)に延長することといたしました。
引き続き皆様からのご提案をお待ち申し上げます。

サイトの性質上、どうしても縦に長くなる中で、背景色に変化をつけることにより、情報ごとのブロックの認識がわかりやすくなったと感じます。また、単純なグリッドデザインでなくなり、変化がついていたところが決定したポイントになります。

この度は、皆様に当コンペにたくさんの素晴らしいデザインをご提案して頂きましてありがとうございました。

```html
<!DOCTYPE html>
<html lang="ja">
<head>
<meta charset="utf-8">
<title>MTS BLOG</title>
<link href="https://fonts.googleapis.com/css2?family=Noto+Sans+JP:wght@400;700&family=Oswald:wght@400;500&display=swap" rel="stylesheet">
<style>
:root{
  --blue:#3b8fcb;
  --blue-dark:#2a6fa6;
  --navy:#1d3f6e;
  --page:#eeeeee;
  --white:#ffffff;
  --orange:#d9622b;
  --text:#444444;
  --muted:#8a8a8a;
  --yellow:#f3cf0a;
  --peach:#f9dccd;
  --sky:#d6ecf6;
  --grey:#dedede;
  --thumb:#eef8f8;
  --teal:#9fd4cf;
  --teal-card:#d3ecea;
  --teal-button:#3f8a86;
  --footer:#f3f3f3;
}
*{margin:0;padding:0;box-sizing:border-box}
html,body{width:1200px;height:3248px;overflow:hidden}
body{background:var(--page);font-family:"Noto Sans JP",sans-serif;color:var(--text);position:relative}
.site-header{height:88px;background:var(--blue);position:relative}
.brand{position:absolute;left:20px;top:0;width:220px;height:88px;background:var(--navy);color:var(--white);display:flex;align-items:center;justify-content:center;font-family:"Oswald",sans-serif;font-size:40px;font-weight:500;letter-spacing:2px}
.site-title{position:absolute;left:268px;top:26px;color:var(--white);font-family:"Oswald",sans-serif;font-size:28px;font-weight:500}
.search{position:absolute;right:60px;top:20px;width:240px;height:34px;background:var(--white);border-radius:17px}
.search svg{position:absolute;right:12px;top:7px}
.banners{position:absolute;left:72px;top:152px;width:1056px;height:456px;display:grid;grid-template-columns:376px 332px 348px;grid-template-rows:228px 228px}
.banner{display:flex;align-items:center;justify-content:center;color:var(--white);font-size:18px}
.banner-main{grid-row:1/3;background:var(--yellow)}
.banner-wide{grid-column:2/4;background:var(--peach)}
.banner-left{background:var(--sky)}
.banner-right{background:var(--grey)}
.archive-tabs{position:absolute;left:72px;top:620px;width:1056px;height:48px;background:var(--blue);display:flex}
.archive-tabs a{flex:1;color:var(--white);text-decoration:none;font-size:17px;display:flex;align-items:center;justify-content:center;border-right:1px solid rgba(255,255,255,.35)}
.archive-tabs a.current{background:var(--blue-dark)}
.archive-tabs a:last-child{flex:.6;border:none}
.posts{position:absolute;left:72px;top:668px;width:1056px;height:1452px;background:var(--white)}
.post{height:290px;display:flex;padding:40px 40px 0;border-bottom:1px solid #ececec}
.post:last-child{border:none}
.thumb{width:200px;height:200px;background:var(--thumb);display:flex;align-items:center;justify-content:center;color:var(--muted);font-size:18px;flex:none}
.post-body{margin-left:40px}
.post-date{color:var(--orange);font-family:"Oswald",sans-serif;font-size:16px}
.post-title{font-size:36px;font-weight:700;color:#333;margin:6px 0 10px;line-height:1.2;white-space:nowrap}
.post-excerpt{font-size:19px;color:var(--muted);line-height:1.55;width:580px}
.read-more{display:inline-block;margin-top:18px;background:var(--orange);color:var(--white);font-family:"Oswald",sans-serif;font-size:15px;padding:0 16px;height:32px;line-height:32px}
.pager{position:absolute;top:2172px;left:0;width:1200px;display:flex;justify-content:center;align-items:center;gap:20px;font-size:15px;color:var(--orange)}
.pager span.page{width:64px;height:64px;background:var(--white);display:flex;align-items:center;justify-content:center;color:#666}
.pager span.page.current{background:var(--orange);color:var(--white)}
.jobs{position:absolute;left:0;top:2280px;width:1200px;height:800px;background:var(--teal)}
.job-grid{position:absolute;left:72px;top:40px;width:1056px;display:grid;grid-template-columns:512px 512px;column-gap:32px;row-gap:42px}
.job-label{font-size:15px;color:var(--white);margin-bottom:8px}
.job-card{height:176px;background:var(--teal-card);border:2px solid rgba(255,255,255,.6);display:flex;align-items:center;padding:0 16px;overflow:hidden}
.job-thumb{width:150px;height:126px;background:var(--white);opacity:.8;display:flex;align-items:center;justify-content:center;color:var(--muted);font-size:14px;flex:none}
.job-body{margin-left:18px;min-width:0}
.job-title{font-size:16px;font-weight:700;color:#3d3d3d;line-height:1.4;white-space:nowrap}
.job-text{font-size:11px;color:#6a7a7a;line-height:1.6;margin:8px 0 10px;white-space:nowrap}
.job-more{display:inline-block;background:var(--teal-button);color:var(--white);font-family:"Oswald",sans-serif;font-size:11px;padding:3px 10px}
.site-footer{position:absolute;left:0;top:3080px;width:1200px;height:168px;background:var(--footer);display:flex;align-items:center;justify-content:center;font-size:15px;color:#999}
</style>
</head>
<body>
<header class="site-header">
  <div class="brand">MTS</div>
  <div class="site-title">MTS BLOG</div>
  <div class="search"><svg width="20" height="20" viewBox="0 0 20 20"><circle cx="8" cy="8" r="6" fill="none" stroke="#3b8fcb" stroke-width="2"/><line x1="12.5" y1="12.5" x2="18" y2="18" stroke="#3b8fcb" stroke-width="2"/></svg></div>
</header>

<section class="banners">
  <div class="banner banner-main" role="img" aria-label="メインバナー">バナー</div>
  <div class="banner banner-wide" role="img" aria-label="バナー">バナー</div>
  <div class="banner banner-left" role="img" aria-label="バナー">バナー</div>
  <div class="banner banner-right" role="img" aria-label="バナー">バナー</div>
</section>

<nav class="archive-tabs">
  <a class="current">2015.03</a><a>2015.02</a><a>2015.01</a><a>2014.12</a><a>2014.11</a><a>2014.10</a><a>2014.09</a><a>&gt;&gt;</a>
</nav>

<main class="posts">
  <article class="post"><div class="thumb" role="img" aria-label="記事のアイキャッチ画像">image</div><div class="post-body"><div class="post-date">UPDATA : 2015.03.01</div><h2 class="post-title">テストです。テストです。テストです。</h2><p class="post-excerpt">テストです。テストです。テストです。テストです。テストです。テストです。テストです。テストです。テストです。テストです。</p><span class="read-more">READ MORE</span></div></article>
  <article class="post"><div class="thumb" role="img" aria-label="記事のアイキャッチ画像">image</div><div class="post-body"><div class="post-date">UPDATA : 2015.03.01</div><h2 class="post-title">テストです。テストです。テストです。</h2><p class="post-excerpt">テストです。テストです。テストです。テストです。テストです。テストです。テストです。テストです。テストです。テストです。</p><span class="read-more">READ MORE</span></div></article>
  <article class="post"><div class="thumb" role="img" aria-label="記事のアイキャッチ画像">image</div><div class="post-body"><div class="post-date">UPDATA : 2015.03.01</div><h2 class="post-title">テストです。テストです。テストです。</h2><p class="post-excerpt">テストです。テストです。テストです。テストです。テストです。テストです。テストです。テストです。テストです。テストです。</p><span class="read-more">READ MORE</span></div></article>
  <article class="post"><div class="thumb" role="img" aria-label="記事のアイキャッチ画像">image</div><div class="post-body"><div class="post-date">UPDATA : 2015.03.01</div><h2 class="post-title">テストです。テストです。テストです。</h2><p class="post-excerpt">テストです。テストです。テストです。テストです。テストです。テストです。テストです。テストです。テストです。テストです。</p><span class="read-more">READ MORE</span></div></article>
  <article class="post"><div class="thumb" role="img" aria-label="記事のアイキャッチ画像">image</div><div class="post-body"><div class="post-date">UPDATA : 2015.03.01</div><h2 class="post-title">テストです。テストです。テストです。</h2><p class="post-excerpt">テストです。テストです。テストです。テストです。テストです。テストです。テストです。テストです。テストです。テストです。</p><span class="read-more">READ MORE</span></div></article>
</main>

<nav class="pager">
  <span>&lt;&lt; 前の5件</span>
  <span class="page current">1</span><span class="page">2</span><span class="page">3</span><span class="page">4</span><span class="page">5</span>
  <span>次の5件 &gt;&gt;</span>
</nav>

<section class="jobs">
  <div class="job-grid">
    <div><div class="job-label">求人情報</div><div class="job-card"><div class="job-thumb" role="img" aria-label="求人画像">image</div><div class="job-body"><div class="job-title">テストです。テストです。テストです。</div><p class="job-text">テストです。テストです。テストです。テストです。<br>テストです。テストです。テストです。テストです。</p><span class="job-more">READ MORE</span></div></div></div>
    <div><div class="job-label">求人情報</div><div class="job-card"><div class="job-thumb" role="img" aria-label="求人画像">image</div><div class="job-body"><div class="job-title">テストです。テストです。テストです。</div><p class="job-text">テストです。テストです。テストです。テストです。<br>テストです。テストです。テストです。テストです。</p><span class="job-more">READ MORE</span></div></div></div>
    <div><div class="job-label">求人情報</div><div class="job-card"><div class="job-thumb" role="img" aria-label="求人画像">image</div><div class="job-body"><div class="job-title">テストです。テストです。テストです。</div><p class="job-text">テストです。テストです。テストです。テストです。<br>テストです。テストです。テストです。テストです。</p><span class="job-more">READ MORE</span></div></div></div>
    <div><div class="job-label">求人情報</div><div class="job-card"><div class="job-thumb" role="img" aria-label="求人画像">image</div><div class="job-body"><div class="job-title">テストです。テストです。テストです。</div><p class="job-text">テストです。テストです。テストです。テストです。<br>テストです。テストです。テストです。テストです。</p><span class="job-more">READ MORE</span></div></div></div>
    <div><div class="job-label">求人情報</div><div class="job-card"><div class="job-thumb" role="img" aria-label="求人画像">image</div><div class="job-body"><div class="job-title">テストです。テストです。テストです。</div><p class="job-text">テストです。テストです。テストです。テストです。<br>テストです。テストです。テストです。テストです。</p><span class="job-more">READ MORE</span></div></div></div>
    <div><div class="job-label">求人情報</div><div class="job-card"><div class="job-thumb" role="img" aria-label="求人画像">image</div><div class="job-body"><div class="job-title">テストです。テストです。テストです。</div><p class="job-text">テストです。テストです。テストです。テストです。<br>テストです。テストです。テストです。テストです。</p><span class="job-more">READ MORE</span></div></div></div>
  </div>
</section>

<footer class="site-footer">Copyright © 2015 Mirabolt Techno Service, Ltd. All rights reserved.</footer>
</body>
</html>
```